tanjak dine in

we are thai, malaysian, vietnamese restaurant. Southeast Asia, we love antique, classic, cozy ambiance, and illustrate arts form.
I would like to design lunch,dinner and limited take out menu a classic, elegant, and fun menu, healthy earthy, feels like in southeast asia

attachment are some example files that you can review it
this is us www.lovetanjak.com
would like to follow http://www.kirinlanternhall.com 's style

restaurants that around the coner,
www.saltpebble.com
http://www.brovanelle.com
http://www.rosatorvans.com
http://www.copperkettleeatery.com

Target Market(s)

neighbourhood, HSC students, modern and hip

Font styles to use
Other font styles liked:
• fonts that match my old menu

Colors
faa54b
fece3e
ebf1f7
acd037
ec2027
000000

Requirements
Nice to have
• insider tips: Don't waste money on lousy food = instant regret
• Keep Calm Curry On

```html
<!DOCTYPE html>
<html lang="en">
<head>
<meta charset="utf-8">
<title>Dine-in Menu</title>
<link href="https://fonts.googleapis.com/css2?family=Arimo:wght@400;700&family=Roboto+Condensed:wght@600&family=Crimson+Pro:wght@400&display=swap" rel="stylesheet">
<style>
:root{
  --band:#d39a55;
  --page:#dde2e7;
  --panel:#f2f3f4;
  --orange:#e9a14a;
  --yellow:#f1c841;
  --green:#acd037;
  --ink:#111111;
  --muted:#333333;
}
*{margin:0;padding:0;box-sizing:border-box}
html,body{width:849px;height:1200px;overflow:hidden}
body{background:var(--page);position:relative;font-family:"Arimo",Arial,sans-serif;color:var(--ink)}
.top-band{position:absolute;left:0;top:0;width:849px;height:102px;background:var(--band)}
.panel{position:absolute;background:var(--panel)}
.corner{position:absolute;left:0;top:0;width:849px;height:1200px;pointer-events:none}
.rule{position:absolute;height:4px;background:var(--green)}
.heading{position:absolute;font-family:"Roboto Condensed","Arial Narrow",sans-serif;font-weight:600;font-size:22px;color:var(--orange);line-height:24px;letter-spacing:-.2px;white-space:nowrap}
.heading small{font-family:"Arimo",Arial,sans-serif;font-weight:700;font-size:14px;letter-spacing:0}
.item{position:absolute;font-size:16px;line-height:17px;white-space:nowrap}
.price{position:absolute;font-size:16px;line-height:17px;color:var(--orange)}
.desc{display:block;white-space:normal;font-family:"Crimson Pro",Georgia,serif;font-size:13px;line-height:17px;color:var(--muted);margin-top:2px;width:250px}
.flower-mark{position:absolute;left:33px;top:1122px;width:18px;height:18px;border-radius:50%;background:#222}
</style>
</head>
<body>
<div class="top-band"></div>

<div class="panel" style="left:23px;top:126px;width:786px;height:375px"></div>
<div class="panel" style="left:23px;top:520px;width:378px;height:224px"></div>
<div class="panel" style="left:23px;top:761px;width:378px;height:399px"></div>
<div class="panel" style="left:440px;top:520px;width:367px;height:640px"></div>

<svg class="corner" viewBox="0 0 849 1200" aria-hidden="true">
  <g fill="var(--yellow)">
    <polygon points="23,126 81,126 23,177"/>
    <polygon points="809,452 809,501 753,501"/>
    <polygon points="401,689 401,744 345,744"/>
    <polygon points="401,1105 401,1160 345,1160"/>
    <polygon points="807,1109 807,1160 750,1160"/>
  </g>
</svg>

<!-- Specialty -->
<div class="rule" style="left:81px;top:167px;width:155px"></div>
<div class="rule" style="left:375px;top:167px;width:402px"></div>
<div class="heading" style="left:247px;top:158px">SPECIALTY</div>

<div class="item" style="left:81px;top:200px">Rendang Nasi Lemak<br>Classic Bowl
  <span class="desc">Coconut-pandanus jasmine rice, rendang curry, hard boiled egg, sambal chili, Pineapple achat, cucumbers and roasted peanuts.</span></div>
<div class="price" style="left:360px;top:200px">€10</div>

<div class="item" style="left:81px;top:319px">Banh Mi Saigon
  <span class="desc">cucumbers, pickled carrots and radishes, home-made Chinese sausage, cilantro, bologna pork pate, hot green chiles.</span></div>
<div class="price" style="left:360px;top:319px">€10</div>

<div class="item" style="left:81px;top:404px">Ka Prao Basil Sauce
  <span class="desc">Garlic, Thai chilli, bell pepper, onion, egg, fresh Thai basil leaves.</span></div>
<div class="price" style="left:360px;top:404px">€10</div>

<div class="item" style="left:472px;top:200px">Cashew Smoked Chilli
  <span class="desc" style="width:235px">Bell pepper, cashew nuts, onion, Thai sweet chilli paste</span></div>
<div class="price" style="left:753px;top:200px">€10</div>

<div class="item" style="left:472px;top:284px">Thai Green Curry
  <span class="desc">Fresh pounded Green chilli paste, lemongrass, bamboo strips, Thai eggplant, bell pepper, long beans, fresh basil</span></div>
<div class="price" style="left:753px;top:284px">€10</div>

<div class="item" style="left:472px;top:370px">Vegeterian Curry Clay Pot
  <span class="desc" style="width:240px">cabbage, potatoes, long beans, carrots, fried tofu, tomatoes, eggplant, fresh chilli</span></div>
<div class="price" style="left:751px;top:370px">€12</div>

<!-- Side order -->
<div class="rule" style="left:81px;top:545px;width:36px"></div>
<div class="rule" style="left:265px;top:545px;width:115px"></div>
<div class="heading" style="left:137px;top:535px">SIDE ORDER</div>
<div class="item" style="left:82px;top:574px">Thai Jasmine Rice</div><div class="price" style="left:360px;top:574px">€1</div>
<div class="item" style="left:81px;top:608px">Coconut Flavored Rice</div><div class="price" style="left:360px;top:608px">€2</div>
<div class="item" style="left:81px;top:642px">Sticky Coconut Rice</div><div class="price" style="left:360px;top:642px">€3</div>
<div class="item" style="left:81px;top:676px">Sambal Egg</div>

<!-- Desserts -->
<div class="rule" style="left:81px;top:784px;width:36px"></div>
<div class="rule" style="left:248px;top:784px;width:128px"></div>
<div class="heading" style="left:137px;top:774px">DESSERTS</div>
<div class="item" style="left:81px;top:815px">Butter Pound Cake<br>Fried Ice Cream</div><div class="price" style="left:360px;top:815px">€3</div>
<div class="item" style="left:81px;top:866px">China Town Style Coffee<br>with Cinnamon Cookies</div><div class="price" style="left:360px;top:866px">€3</div>
<div class="item" style="left:81px;top:917px">Coconut Jam &amp; Butter<br>Toast</div><div class="price" style="left:360px;top:917px">€3</div>
<div class="item" style="left:81px;top:969px">Coconut Cream</div><div class="price" style="left:360px;top:969px">€3</div>
<div class="item" style="left:81px;top:1003px">Mango Sticky Rice</div><div class="price" style="left:360px;top:1003px">€3</div>
<div class="item" style="left:81px;top:1037px">Classic Shaved Ice with<br>Rose syrup and Palm<br>Sugar ice cream</div><div class="price" style="left:360px;top:1037px">€3</div>
<div class="flower-mark" role="img" aria-label="Small flower ornament"></div>

<!-- Hot beverages -->
<div class="rule" style="left:469px;top:545px;width:84px"></div>
<div class="rule" style="left:750px;top:545px;width:43px"></div>
<div class="heading" style="left:586px;top:535px">HOT BEVERAGES</div>
<div class="item" style="left:474px;top:574px">Viet Style Hot Coffee</div><div class="price" style="left:749px;top:574px">€3</div>
<div class="item" style="left:474px;top:608px">Hand Pulled Milk Tea</div><div class="price" style="left:749px;top:608px">€3</div>
<div class="item" style="left:474px;top:642px">Oolong Tea</div><div class="price" style="left:749px;top:642px">€3</div>
<div class="item" style="left:474px;top:676px">Green Tea</div><div class="price" style="left:749px;top:676px">€3</div>

<!-- Cold beverages -->
<div class="rule" style="left:474px;top:716px;width:88px"></div>
<div class="rule" style="left:760px;top:716px;width:43px"></div>
<div class="heading" style="left:587px;top:706px">COLD BEVERAGES</div>
<div class="item" style="left:474px;top:746px">Origina Sparkling Citrus</div><div class="price" style="left:749px;top:746px">€3</div>
<div class="item" style="left:474px;top:780px">Calamansi Honey Jasmine Tea</div><div class="price" style="left:749px;top:780px">€3</div>
<div class="item" style="left:474px;top:814px">Fresh Coconut Juice</div><div class="price" style="left:749px;top:814px">€3</div>
<div class="item" style="left:474px;top:848px">Fresh Mango Passion Fruits<br>Smoothie</div><div class="price" style="left:749px;top:848px">€3</div>
<div class="item" style="left:474px;top:899px">Thai Iced Tea</div><div class="price" style="left:749px;top:899px">€3</div>
<div class="item" style="left:474px;top:933px">Viet Ice Coffee</div><div class="price" style="left:749px;top:933px">€3</div>

<!-- Beer -->
<div class="rule" style="left:475px;top:989px;width:73px"></div>
<div class="rule" style="left:717px;top:989px;width:86px"></div>
<div class="heading" style="left:586px;top:980px">BEER <small>€3 for all</small></div>
<div class="item" style="left:474px;top:1019px">Delta Gold</div><div class="item" style="left:679px;top:1019px">Harimau</div>
<div class="item" style="left:474px;top:1053px">Lotus Pale</div><div class="item" style="left:679px;top:1053px">Harbor Lager</div>
<div class="item" style="left:474px;top:1087px">Palm Coast</div><div class="item" style="left:679px;top:1087px">Snowpeak</div>
<div class="item" style="left:474px;top:1121px">Compass Ale</div>
</body>
</html>
```